Hair extensions packaging design

Professional hair extensions packaging design.
We like a clean and crisp look. The design should convey luxury and highest quality.

Target Market(s)

women ages 16-40

Industry/Entity Type

beauty, hair

Other font styles liked:
• kiona

Requirements
Must have
• clean, crisp, professional look

```html
<!DOCTYPE html>
<html lang="en">
<head>
<meta charset="utf-8">
<title>Velmora Hair Extension Box</title>
<link href="https://fonts.googleapis.com/css2?family=Oswald:wght@300;400;500&display=swap" rel="stylesheet">
<style>
  :root {
    --stage: #e7e7e8;
    --box: #222223;
    --box-deep: #18181a;
    --side: #121213;
    --gold: #d9a544;
    --gold-light: #f3cd78;
    --copper: #9c4f1f;
    --brown-cell: #8a4a1a;
    --ink-light: #f2f2f2;
    --window-grey: #707072;
  }
  * { margin: 0; padding: 0; box-sizing: border-box; }
  html, body { width: 1200px; height: 889px; overflow: hidden; }
  body {
    background: var(--stage);
    font-family: "Oswald", "Arial Narrow", sans-serif;
    position: relative;
  }

  /* Side panel */
  .box-side {
    position: absolute;
    left: 492px; top: 24px;
    width: 30px; height: 840px;
    background: linear-gradient(90deg, #0d0d0e, var(--side) 60%, #1c1c1d);
    overflow: hidden;
    color: var(--ink-light);
  }
  .side-brand {
    position: absolute; top: 66px; left: 50%;
    transform: translateX(-50%);
    writing-mode: vertical-rl;
    font-size: 10px; font-weight: 300; letter-spacing: 2px; color: var(--gold);
    display: flex; align-items: center; gap: 5px;
  }
  .side-brand-dot { width: 5px; height: 5px; border-radius: 50%; background: var(--gold); }
  .side-headline {
    position: absolute; top: 290px; left: 50%;
    transform: translateX(-50%);
    writing-mode: vertical-rl;
    line-height: 1;
    display: flex; flex-direction: row-reverse; gap: 1px;
  }
  .side-headline .main { font-size: 10px; font-weight: 400; }
  .side-headline .sub { font-size: 6px; font-weight: 400; }
  .side-hair {
    position: absolute; top: 447px; left: 5px;
    width: 14px; height: 222px;
    border-radius: 50%;
    background: linear-gradient(180deg, #4a2c17, #a06a3e 40%, #c08a5a 70%, #6b4124);
  }
  .side-footer {
    position: absolute; top: 794px; left: 50%;
    transform: translateX(-50%);
    writing-mode: vertical-rl;
    font-size: 6px; font-weight: 400;
  }

  /* Front face */
  .box-front {
    position: absolute;
    left: 522px; top: 24px;
    width: 187px; height: 840px;
    background: linear-gradient(160deg, #2a2a2b 0%, var(--box) 45%, var(--box-deep) 100%);
    overflow: hidden;
    color: var(--ink-light);
    text-align: center;
  }
  .brand {
    position: absolute; top: 100px; left: 0; width: 100%;
    display: flex; align-items: center; justify-content: center; gap: 7px;
    font-weight: 300; font-size: 18px; letter-spacing: 2px; color: var(--gold);
  }
  .brand-dot { width: 8px; height: 8px; border-radius: 50%; background: var(--gold); }
  .tagline {
    position: absolute; top: 154px; left: 0; width: 100%;
    font-size: 10px; font-weight: 400; color: var(--gold); letter-spacing: 0.1px;
  }
  .window {
    position: absolute; top: 199px; left: 0; width: 187px; height: 400px;
  }
  .shade-badge {
    position: absolute; left: 61px; top: 503px;
    width: 64px; height: 64px; border-radius: 50%;
    background: #111;
    border: 3px solid var(--gold);
    box-shadow: 0 0 0 2px var(--copper);
    display: flex; align-items: center; justify-content: center;
    font-size: 10px; line-height: 1.1; font-weight: 500; color: #fff;
  }
  .headline { position: absolute; top: 606px; left: 0; width: 100%; }
  .headline .main { font-size: 27px; font-weight: 400; line-height: 34px; }
  .headline .sub { font-size: 15px; font-weight: 400; line-height: 28px; }
  .spec-table {
    position: absolute; top: 712px; left: 37px;
    border-collapse: separate; border-spacing: 3px 6px;
  }
  .spec-table th {
    width: 54px; height: 15px;
    background: linear-gradient(180deg, var(--gold-light), var(--copper) 70%, var(--gold));
    font-size: 9px; font-weight: 400; color: #fff; text-align: left; padding-left: 14px;
  }
  .spec-table td {
    width: 62px; height: 15px;
    background: var(--brown-cell);
    font-size: 6.5px; color: #fff; vertical-align: top; padding-top: 1px;
  }
  .pack-weight {
    position: absolute; top: 804px; left: 0; width: 100%;
    font-size: 12px; font-weight: 400;
  }
</style>
</head>
<body>
  <aside class="box-side">
    <div class="side-brand"><span class="side-brand-dot"></span>VELMORA</div>
    <div class="side-headline">
      <span class="main">100% VIRGIN</span>
      <span class="sub">REMI HUMAN HAIR</span>
      <span class="sub">EXTENTION</span>
    </div>
    <div class="side-hair" role="img" aria-label="Strip of straight brown hair extension"></div>
    <p class="side-footer">REMI HUMAN HAIR</p>
  </aside>

  <main class="box-front">
    <div class="brand"><span class="brand-dot"></span>VELMORA</div>
    <p class="tagline">LUXURY . 100% REMI . HAIR COUTURE</p>

    <svg class="window" viewBox="0 0 187 400" xmlns="http://www.w3.org/2000/svg">
      <defs>
        <linearGradient id="hairTone" x1="0" y1="0" x2="1" y2="0">
          <stop offset="0" stop-color="#9c6a40"/>
          <stop offset="0.35" stop-color="#c9996b"/>
          <stop offset="0.55" stop-color="#a8774b"/>
          <stop offset="0.8" stop-color="#c08c5c"/>
          <stop offset="1" stop-color="#8f6139"/>
        </linearGradient>
        <linearGradient id="ringGold" x1="1" y1="0" x2="0" y2="1">
          <stop offset="0" stop-color="#f7d27a"/>
          <stop offset="0.3" stop-color="#d58a2c"/>
          <stop offset="0.65" stop-color="#7a2e14"/>
          <stop offset="1" stop-color="#8a3a1c"/>
        </linearGradient>
        <clipPath id="windowClip">
          <path d="M187 12 C110 20 20 120 8 240 C4 320 20 380 50 392 C120 380 170 320 187 230 Z"/>
        </clipPath>
      </defs>
      <path d="M187 12 C110 20 20 120 8 240 C4 320 20 380 50 392 C120 380 170 320 187 230 Z" fill="var(--window-grey)"/>
      <g clip-path="url(#windowClip)">
        <rect x="10" y="16" width="172" height="376" fill="url(#hairTone)" role="img" aria-label="Straight medium light brown hair extension"/>
      </g>
      <path d="M187 4 C100 10 14 120 3 250 C0 330 8 390 2 398" fill="none" stroke="url(#ringGold)" stroke-width="6"/>
      <path d="M187 232 C174 320 130 378 60 396" fill="none" stroke="var(--gold)" stroke-width="4"/>
    </svg>

    <div class="shade-badge">Medium<br>Light<br>Brown</div>

    <div class="headline">
      <p class="main">100% VIRGIN</p>
      <p class="sub">REMI HUMAN HAIR</p>
      <p class="sub">EXTENTION</p>
    </div>

    <table class="spec-table">
      <tr><th>COLOR</th><td>medium light brown</td></tr>
      <tr><th>LENGTH</th><td></td></tr>
      <tr><th>STYLE</th><td></td></tr>
    </table>

    <p class="pack-weight">100g Per Pack</p>
  </main>
</body>
</html>
```